Prestige Car Bodyshop Business Card

We are a car bodyshop based in the UK. Our customer base is mainly prestige high-value vehicles. I am looking for a classy and stylish business card design for my staff to give out to customers, with their direct email and phone number, as well as our main email and phone number with address details

I am also looking to have a general business card design with just our main company address and contact details, but also have a space to add a manufacturer approval logo (i.e Velmora, Orek, Tovalo etc... logo) in the corner somewhere.

I do not particularly want any outlines or pictures of cars on the card, I would just like a quality high-end look.

Please feel free to get in touch if you have any questions or queries?

Many Thanks

Malcolm

Target Market(s)

Prestige vehicle owners

Industry/Entity Type

Automotive

Contact Information for Business Card

I am looking for a classy and stylish business card design for my staff to give out to customers, with their direct email and phone number, as well as our main email and phone number with address details

Font styles to use
Sans Serif

Colors

Designer to choose colors to be used in the design.

Requirements
Nice to have
• I do not particularly want any outlines or pictures of cars on the card, I would just like a quality high-end look.

```html
<!DOCTYPE html>
<html lang="en">
<head>
<meta charset="utf-8">
<title>Ashcombe Accident Repair Centre – Business Cards</title>
<link href="https://fonts.googleapis.com/css2?family=Lato:wght@300;400;700&display=swap" rel="stylesheet">
<style>
  :root {
    --page: #ffffff;
    --card-light: #f2f2f2;
    --navy: #1b3a6e;
    --navy-deep: #1a3466;
    --blue: #1668b8;
    --orange: #f08a2c;
    --ink: #1d3566;
    --white: #ffffff;
    --badge: #c9cdd3;
    --badge-alt: #b3b9c2;
  }
  * { margin: 0; padding: 0; box-sizing: border-box; }
  html, body { width: 1200px; height: 904px; overflow: hidden; background: var(--page); }
  body { position: relative; font-family: "Lato", sans-serif; }

  .card { position: absolute; width: 385px; height: 234px; overflow: hidden; }
  .card--front-a { left: 208px; top: 199px; background: var(--card-light); }
  .card--front-b { left: 609px; top: 199px; }
  .card--back-a { left: 208px; top: 457px; }
  .card--back-b { left: 609px; top: 457px; }
  .card--back { background: linear-gradient(200deg, var(--blue) 0%, #1a57a0 35%, var(--navy-deep) 75%); color: var(--white); }

  .front-backdrop { position: absolute; inset: 0; background: radial-gradient(circle at 50% 40%, #f3f3f3 0%, #ececee 100%); }

  /* Brand lockup */
  .lockup { position: absolute; }
  .lockup__mark { position: absolute; border-radius: 50%; background: var(--navy); }
  .lockup__name { position: absolute; font-weight: 300; color: var(--ink); white-space: nowrap; letter-spacing: 0.5px; }
  .lockup__rule { position: absolute; height: 1px; background: var(--ink); }
  .lockup__tag { position: absolute; font-weight: 400; color: var(--ink); white-space: nowrap; letter-spacing: 0.4px; }
  .card--back .lockup__mark { background: transparent; border: 1px solid var(--white); }
  .card--back .lockup__name, .card--back .lockup__tag { color: var(--white); }
  .card--back .lockup__rule { background: var(--white); }

  /* Approved manufacturer strip */
  .approvals { position: absolute; left: 37px; top: 200px; width: 314px; height: 24px; display: flex; align-items: center; justify-content: space-between; }
  .approvals__badge { display: block; height: 16px; background: var(--badge); }
  .approvals__badge--round { width: 18px; height: 18px; border-radius: 50%; background: var(--badge-alt); }
  .approvals__badge--oval { border-radius: 50%; }

  /* Contact block */
  .divider { position: absolute; width: 1px; background: rgba(255,255,255,0.75); }
  .contact { position: absolute; font-size: 10.5px; line-height: 1; letter-spacing: 0.2px; }
  .contact__line { position: absolute; left: 0; white-space: nowrap; }
  .contact__icon { position: absolute; left: -11px; top: 0; width: 8px; height: 9px; }
  .contact__web { font-size: 11px; }
  .staff__name { position: absolute; font-weight: 700; font-size: 13px; white-space: nowrap; }
  .staff__role { position: absolute; font-size: 10.5px; white-space: nowrap; }

  .social { position: absolute; width: 18px; height: 18px; border-radius: 50%; border: 1px solid var(--white); }
</style>
</head>
<body>

<!-- Front, plain -->
<section class="card card--front-a">
  <div class="lockup">
    <span class="lockup__mark" style="left:83px;top:69px;width:74px;height:74px;"></span>
    <span class="lockup__name" style="left:165px;top:80px;font-size:29px;">ASHCOMBE</span>
    <span class="lockup__rule" style="left:165px;top:114px;width:136px;"></span>
    <span class="lockup__tag" style="left:166px;top:119px;font-size:10px;">ACCIDENT REPAIR CENTRE</span>
  </div>
  <div class="approvals" aria-label="Approved manufacturer badges">
    <span class="approvals__badge approvals__badge--oval" style="width:30px;height:12px;"></span>
    <span class="approvals__badge approvals__badge--oval" style="width:36px;height:16px;"></span>
    <span class="approvals__badge" style="width:38px;height:12px;"></span>
    <span class="approvals__badge approvals__badge--oval" style="width:36px;height:15px;"></span>
    <span class="approvals__badge" style="width:20px;height:10px;"></span>
    <span class="approvals__badge" style="width:24px;height:14px;"></span>
    <span class="approvals__badge" style="width:46px;height:8px;"></span>
    <span class="approvals__badge approvals__badge--round"></span>
    <span class="approvals__badge approvals__badge--round"></span>
  </div>
</section>

<!-- Front, patterned backdrop -->
<section class="card card--front-b">
  <div class="front-backdrop" role="img" aria-label="Soft grey backdrop with a faint repeating brand-mark pattern"></div>
  <div class="lockup">
    <span class="lockup__mark" style="left:171px;top:54px;width:44px;height:44px;"></span>
    <span class="lockup__name" style="left:220px;top:61px;font-size:18px;">ASHCOMBE</span>
    <span class="lockup__rule" style="left:220px;top:83px;width:81px;"></span>
    <span class="lockup__tag" style="left:221px;top:86px;font-size:6.5px;">ACCIDENT REPAIR CENTRE</span>
  </div>
  <div class="approvals" aria-label="Approved manufacturer badges">
    <span class="approvals__badge approvals__badge--oval" style="width:30px;height:12px;"></span>
    <span class="approvals__badge approvals__badge--oval" style="width:36px;height:16px;"></span>
    <span class="approvals__badge" style="width:38px;height:12px;"></span>
    <span class="approvals__badge approvals__badge--oval" style="width:36px;height:15px;"></span>
    <span class="approvals__badge" style="width:20px;height:10px;"></span>
    <span class="approvals__badge" style="width:24px;height:14px;"></span>
    <span class="approvals__badge" style="width:46px;height:8px;"></span>
    <span class="approvals__badge approvals__badge--round"></span>
    <span class="approvals__badge approvals__badge--round"></span>
  </div>
</section>

<!-- Back, general -->
<section class="card card--back card--back-a">
  <div class="lockup">
    <span class="lockup__mark" style="left:37px;top:96px;width:42px;height:42px;"></span>
    <span class="lockup__name" style="left:84px;top:103px;font-size:15px;">ASHCOMBE</span>
    <span class="lockup__rule" style="left:84px;top:122px;width:80px;"></span>
    <span class="lockup__tag" style="left:84px;top:125px;font-size:6px;">ACCIDENT REPAIR CENTRE</span>
  </div>
  <span class="divider" style="left:188px;top:52px;height:130px;"></span>
  <div class="contact" style="left:209px;top:0;">
    <span class="contact__line" style="top:58px;">
      <svg class="contact__icon" viewBox="0 0 8 10"><path d="M4 0a3.5 3.5 0 0 0-3.5 3.5C.5 6 4 10 4 10s3.5-4 3.5-6.5A3.5 3.5 0 0 0 4 0zm0 5a1.4 1.4 0 1 1 0-2.8A1.4 1.4 0 0 1 4 5z" fill="#fff"/></svg>
      Fernleigh Road, Kingsmead</span>
    <span class="contact__line" style="top:73px;">Hallowford, Bristol, BS41 7RX</span>
    <span class="contact__line" style="top:108px;">
      <svg class="contact__icon" viewBox="0 0 8 8"><path d="M0 2.5C0 1 1.5 0 4 0s4 1 4 2.5v.7H6V2.2C5.4 2 4.7 1.9 4 1.9S2.6 2 2 2.2v1H0zM1.3 4 2.5 3h3l1.2 1v4H1.3z" fill="#fff"/></svg>
      0117 496 0418</span>
    <span class="contact__line" style="top:123px;">
      <svg class="contact__icon" viewBox="0 0 8 8"><rect x="0.5" y="2.5" width="7" height="5" fill="#fff"/><rect x="2" y="0.5" width="4" height="2" fill="#fff"/></svg>
      0117 496 0732</span>
    <span class="contact__line" style="top:138px;">
      <svg class="contact__icon" viewBox="0 0 8 8"><rect x="0.5" y="1.5" width="7" height="5" fill="none" stroke="#fff" stroke-width="0.8"/><path d="M.5 1.5 4 4.5l3.5-3" fill="none" stroke="#fff" stroke-width="0.8"/></svg>
      info@ashcombe.co.uk</span>
    <span class="contact__line contact__web" style="top:161px;">www.ashcombe.co.uk</span>
  </div>
  <span class="social" style="left:317px;top:203px;" aria-label="Social profile"></span>
  <span class="social" style="left:345px;top:203px;" aria-label="Social profile"></span>
</section>

<!-- Back, staff -->
<section class="card card--back card--back-b">
  <div class="lockup">
    <span class="lockup__mark" style="left:37px;top:96px;width:42px;height:42px;"></span>
    <span class="lockup__name" style="left:84px;top:103px;font-size:15px;">ASHCOMBE</span>
    <span class="lockup__rule" style="left:84px;top:122px;width:80px;"></span>
    <span class="lockup__tag" style="left:84px;top:125px;font-size:6px;">ACCIDENT REPAIR CENTRE</span>
  </div>
  <span class="divider" style="left:189px;top:60px;height:114px;"></span>
  <span class="staff__name" style="left:199px;top:45px;">John Doe</span>
  <span class="staff__role" style="left:199px;top:63px;">Manager</span>
  <div class="contact" style="left:210px;top:0;">
    <span class="contact__line" style="top:101px;">
      <svg class="contact__icon" viewBox="0 0 8 10"><path d="M4 0a3.5 3.5 0 0 0-3.5 3.5C.5 6 4 10 4 10s3.5-4 3.5-6.5A3.5 3.5 0 0 0 4 0zm0 5a1.4 1.4 0 1 1 0-2.8A1.4 1.4 0 0 1 4 5z" fill="#fff"/></svg>
      Fernleigh Road, Kingsmead</span>
    <span class="contact__line" style="top:116px;">Hallowford, Bristol, BS41 7RX</span>
    <span class="contact__line" style="top:131px;">
      <svg class="contact__icon" viewBox="0 0 8 8"><path d="M0 2.5C0 1 1.5 0 4 0s4 1 4 2.5v.7H6V2.2C5.4 2 4.7 1.9 4 1.9S2.6 2 2 2.2v1H0zM1.3 4 2.5 3h3l1.2 1v4H1.3z" fill="#fff"/></svg>
      0117 496 0418</span>
    <span class="contact__line" style="top:146px;">
      <svg class="contact__icon" viewBox="0 0 8 8"><rect x="0.5" y="2.5" width="7" height="5" fill="#fff"/><rect x="2" y="0.5" width="4" height="2" fill="#fff"/></svg>
      0117 496 0732</span>
    <span class="contact__line" style="top:161px;">
      <svg class="contact__icon" viewBox="0 0 8 8"><rect x="0.5" y="1.5" width="7" height="5" fill="none" stroke="#fff" stroke-width="0.8"/><path d="M.5 1.5 4 4.5l3.5-3" fill="none" stroke="#fff" stroke-width="0.8"/></svg>
      info@ashcombe.co.uk</span>
  </div>
  <span class="contact__web" style="position:absolute;left:199px;top:183px;white-space:nowrap;">www.ashcombe.co.uk</span>
  <span class="social" style="left:318px;top:199px;" aria-label="Social profile"></span>
  <span class="social" style="left:346px;top:199px;" aria-label="Social profile"></span>
</section>

</body>
</html>
```